First Aid Training business needs business card design

We would like a double sided business card designed for a first aid training business - Banksia First Aid. We provide first aid training and , WHS (work, health and safety) training.

The attached word document contains the key information we would like on each side of the business card.

Final design needs to be delivered in print ready format, along with the original file.

```html
<!DOCTYPE html>
<html lang="en">
<head>
<meta charset="utf-8">
<title>Banksia First Aid – Business Card</title>
<link href="https://fonts.googleapis.com/css2?family=Montserrat:wght@400;500;700;800&display=swap" rel="stylesheet">
<style>
  :root {
    --page: #ececec;
    --paper: #f6f6f6;
    --grey: #8c8c8c;
    --red: #e1232a;
    --ink: #111111;
    --white: #ffffff;
  }
  * { box-sizing: border-box; margin: 0; padding: 0; }
  html, body { width: 1200px; height: 900px; overflow: hidden; }
  body {
    background: var(--page);
    font-family: "Montserrat", sans-serif;
    display: flex; flex-direction: column; align-items: center; justify-content: center;
    gap: 50px;
  }
  .card {
    position: relative; width: 560px; height: 320px;
    background: var(--paper);
    box-shadow: 0 10px 30px rgba(0,0,0,.15);
    overflow: hidden;
  }
  .card__art { position: absolute; inset: 0; width: 100%; height: 100%; }
  .brand { position: absolute; display: flex; align-items: center; gap: 16px; }
  .brand__dot { width: 56px; height: 56px; border-radius: 50%; background: var(--red); flex: none; }
  .brand__name { font-weight: 700; color: var(--ink); text-transform: uppercase; line-height: 1.1; }

  /* front */
  .card--front .brand { left: 36px; top: 34px; }
  .card--front .brand__name { font-size: 24px; letter-spacing: 1px; }
  .services {
    position: absolute; left: 40px; top: 190px; list-style: none;
    color: var(--white); font-size: 13px; line-height: 1.6;
  }
  .services li::before { content: "• "; }
  .benefits {
    position: absolute; right: 30px; bottom: 22px; text-align: right;
    color: var(--white); font-size: 12.5px; line-height: 1.55;
  }
  .benefits__lead { font-weight: 700; font-size: 13.5px; margin-bottom: 4px; }
  .benefits li { list-style: none; }
  .benefits li::after { content: " •"; }

  /* back */
  .person {
    position: absolute; left: 40px; top: 36px;
    font-weight: 800; font-size: 28px; line-height: 1.05; color: var(--ink);
    text-transform: uppercase;
  }
  .contacts {
    position: absolute; left: 26px; top: 150px; list-style: none;
    color: var(--white); font-size: 13px; line-height: 1.9; font-weight: 500;
    text-transform: uppercase;
  }
  .contacts li { display: flex; align-items: center; gap: 9px; }
  .contacts svg { width: 18px; height: 18px; flex: none; }
  .card--back .brand { right: 30px; top: 60px; flex-direction: column; gap: 10px; }
  .card--back .brand__dot { width: 90px; height: 90px; background: var(--grey); }
  .card--back .brand__name { font-size: 15px; text-align: center; }
</style>
</head>
<body>

<section class="card card--front" aria-label="Card front">
  <svg class="card__art" viewBox="0 0 560 320" preserveAspectRatio="none">
    <path d="M0,80 C40,170 180,150 320,150 C440,150 520,152 560,165 L560,320 L0,320 Z" fill="var(--grey)"/>
    <path d="M250,149 C400,144 510,150 560,160 L560,172 C510,157 400,150 250,149 Z" fill="var(--ink)"/>
  </svg>
  <div class="brand">
    <span class="brand__dot"></span>
    <span class="brand__name">Banksia<br>First Aid Training</span>
  </div>
  <ul class="services">
    <li>First Aid Training</li>
    <li>WHS Training</li>
  </ul>
  <div class="benefits">
    <p class="benefits__lead">Onsite Training<br>- We can come to you</p>
    <ul>
      <li>Time efficient</li>
      <li>Minimise downtime for your team</li>
      <li>Cost effective</li>
    </ul>
  </div>
</section>

<section class="card card--back" aria-label="Card back">
  <svg class="card__art" viewBox="0 0 560 320" preserveAspectRatio="none">
    <path d="M0,110 C220,115 335,150 375,230 C400,275 450,285 560,280 L560,320 L0,320 Z" fill="var(--red)"/>
    <path d="M0,98 C220,103 340,140 378,218 C325,150 220,112 0,106 Z" fill="var(--ink)"/>
  </svg>
  <h1 class="person">Liam<br>Harper</h1>
  <ul class="contacts">
    <li><svg viewBox="0 0 20 20"><circle cx="10" cy="10" r="10" fill="var(--white)"/><path d="M7 5l2 3-1.2 1.2a6 6 0 0 0 3 3L12 11l3 2-1 2c-4 0-9-5-9-9z" fill="var(--red)"/></svg>0491 570 226</li>
    <li><svg viewBox="0 0 20 20"><circle cx="10" cy="10" r="10" fill="var(--white)"/><rect x="5" y="6.5" width="10" height="7" fill="none" stroke="var(--red)" stroke-width="1.4"/><path d="M5 6.5l5 4 5-4" fill="none" stroke="var(--red)" stroke-width="1.4"/></svg>help@banksiafirstaid.com.au</li>
    <li><svg viewBox="0 0 20 20"><circle cx="10" cy="10" r="10" fill="var(--white)"/><circle cx="10" cy="10" r="5.5" fill="none" stroke="var(--red)" stroke-width="1.4"/><path d="M4.5 10h11M10 4.5c-3 3-3 8 0 11M10 4.5c3 3 3 8 0 11" fill="none" stroke="var(--red)" stroke-width="1.2"/></svg>www.banksiafirstaid.com.au</li>
  </ul>
  <div class="brand">
    <span class="brand__dot"></span>
    <span class="brand__name">Banksia<br>First Aid</span>
  </div>
</section>

</body>
</html>
```